Zielgruppe
Wir sind eine Wäscherei.
Zielgruppe: Kunden aus der Hotel- und Gastronomiebranche
Aufgabenstellung
Wir benötigen einen 2-seitigen Flyer DIN lang. 9,8 x21cm
TextInhalte sind in der Vorlage-Datei.
Bilder sind eingefügt.

```html
<!DOCTYPE html>
<html lang="de">
<head>
<meta charset="utf-8">
<title>Wäscherei Talbrunn – Flyer DIN lang</title>
<link rel="stylesheet" href="https://fonts.googleapis.com/css2?family=Open+Sans:wght@300;400;600;700&display=swap">
<style>
  :root{
    --magenta:#e5188b;
    --graphite:#58585a;
    --text:#4a4a4c;
    --soft-text:#6a6a6c;
    --paper-shade:#d9d9da;
    --stage:#ecebe8;
  }
  *{box-sizing:border-box;margin:0;padding:0}
  html,body{width:1200px;height:1200px;overflow:hidden;background:var(--stage);font-family:"Open Sans",sans-serif;color:var(--text)}
  .flyer{position:absolute;left:35px;width:1145px;height:540px;overflow:hidden;
    background:radial-gradient(ellipse at 65% 45%,#ffffff 0%,#efefef 45%,var(--paper-shade) 100%);
    box-shadow:0 2px 6px rgba(0,0,0,.18)}
  .flyer--front{top:27px}
  .flyer--back{top:611px;background:radial-gradient(ellipse at 35% 50%,#ffffff 0%,#f0f0f0 50%,var(--paper-shade) 100%)}
  .shape{position:absolute;inset:0;width:1145px;height:540px;z-index:2}
  .band{position:absolute;background:var(--magenta);z-index:1}
  .headline{position:absolute;z-index:3;color:#fff;font-weight:400;white-space:nowrap;line-height:1;letter-spacing:2px}
  .headline .lead{font-weight:300;font-size:40px;letter-spacing:2px;margin-right:12px}
  .headline .big{font-size:64px}
  .brand{position:absolute;z-index:3;font-weight:700;color:var(--magenta);letter-spacing:.5px;white-space:nowrap}
  .contact{position:absolute;z-index:3;font-weight:400;color:var(--soft-text);white-space:nowrap}
  /* front */
  .badge{position:absolute;z-index:4;left:979px;top:119px;width:151px;height:151px;border-radius:50%;
    background:#fff;border:3px solid var(--magenta);text-align:center}
  .badge .neu{display:block;font-size:54px;color:var(--magenta);line-height:1;margin-top:22px;letter-spacing:2px}
  .badge .when{display:block;font-size:18px;color:var(--graphite);line-height:1;margin-top:-4px}
  .intro{position:absolute;z-index:3;left:541px;top:279px;font-size:16px;line-height:23px;font-weight:300;color:var(--text);white-space:nowrap}
  .intro b{font-weight:600}
  .intro .claim{margin-top:23px}
  .note{position:absolute;z-index:3;left:486px;top:438px;font-size:11px;line-height:16px;color:var(--soft-text);white-space:nowrap}
  .note .min{margin-top:16px}
  .price{position:absolute;z-index:3;top:437px;height:110px;border-radius:14px 14px 0 0;color:#fff;padding:22px 10px 0 12px}
  .price--pink{left:726px;width:172px;background:var(--magenta)}
  .price--grey{left:910px;width:201px;background:var(--graphite)}
  .price .forms{font-size:14px;font-weight:600;white-space:nowrap}
  .price .amount{font-size:20px;font-weight:400;margin-top:2px;white-space:nowrap}
  .price .amount strong{font-size:30px;font-weight:700}
  .price .per{font-size:11px;text-align:right;padding-right:22px;margin-top:-4px}
  .vat{position:absolute;z-index:3;left:1117px;top:520px;font-size:10px;color:#8a8a8c;transform:rotate(-90deg);transform-origin:0 0;white-space:nowrap}
  /* back */
  .services{position:absolute;z-index:3;top:262px;list-style:none;font-size:16px;color:var(--text)}
  .services--left{left:54px}
  .services--right{left:383px}
  .services li{position:relative;padding-left:18px;line-height:19px;margin-bottom:11px}
  .services li svg{position:absolute;left:0;top:-3px}
</style>
</head>
<body>

<section class="flyer flyer--front" aria-label="Vorderseite Servietten-Faltservice">
  <div class="band" style="left:470px;top:96px;width:675px;height:62px"></div>
  <div class="band" style="left:480px;top:165px;width:665px;height:62px"></div>

  <svg class="shape" viewBox="0 0 1145 540" aria-hidden="true">
    <path d="M0 0 H300 C560 150 540 400 395 540 H0Z" fill="var(--graphite)"/>
    <path d="M0 0 H480 C520 120 470 360 360 540 H0Z" fill="var(--magenta)"/>
  </svg>
  <svg class="shape" viewBox="0 0 1145 540" role="img" aria-label="Foto: gefaltete lila Stoffserviette auf gedecktem Tisch mit Weinglas und Besteck">
    <defs>
      <linearGradient id="napkinPhoto" x1="0" y1="0" x2="1" y2="1">
        <stop offset="0" stop-color="#cfc6d6"/>
        <stop offset=".35" stop-color="#b89fcf"/>
        <stop offset=".7" stop-color="#4a4048"/>
        <stop offset="1" stop-color="#d8d6d4"/>
      </linearGradient>
    </defs>
    <path d="M0 0 H375 C470 110 520 330 370 540 H0Z" fill="url(#napkinPhoto)"/>
  </svg>

  <div class="brand" style="left:655px;top:40px;font-size:24px">Wäscherei Talbrunn</div>
  <div class="contact" style="left:926px;top:26px;font-size:12px;line-height:17px">
    Lindenweg 12 – 70999 Talbrunn<br>
    Tel. +49 (0) 7100 / 23 56 80<br>
    E-Mail. info@waescherei-talbrunn.de
  </div>

  <h1 class="headline" style="left:500px;top:100px"><span class="lead">IHR</span><span class="big">SERVIETTEN-</span></h1>
  <div class="headline" style="left:546px;top:167px"><span class="big" style="font-size:62px">FALTSERVICE</span></div>

  <div class="badge"><span class="neu">NEU</span><span class="when">ab November</span></div>

  <div class="intro">
    <p>Wir <b>optimieren</b> Ihren Serviettenfaltprozess.</p>
    <p>Wir <b>entlasten</b> Sie von dieser demotivierenden und unproduktiven Tätigkeit.</p>
    <p>Wir falten Ihnen Ihre Stoffservietten oder unsere Mietservietten vor.</p>
    <p class="claim"><b>Hygienisch, zuverlässig und wirtschaftlich</b> – bereit für die Mise en Place.</p>
  </div>

  <div class="note">
    <p>Weitere Formen sind auf Anfrage möglich.</p>
    <p>Bei Bedarf stellen wir Ihnen</p>
    <p>Mietservietten für nur 0,25 €*</p>
    <p>je Stück zur Verfügung.</p>
    <p class="min">Mindestabnahmemenge: 100 Stück</p>
  </div>

  <div class="price price--pink">
    <div class="forms">Welle, Kerze, Fächer</div>
    <div class="amount">nur <strong>0,20 €</strong> *</div>
    <div class="per">je Faltung</div>
  </div>
  <div class="price price--grey">
    <div class="forms">Pyramide, Bischofsmütze</div>
    <div class="amount">nur <strong>0,35 €</strong> *</div>
    <div class="per">je Faltung</div>
  </div>
  <div class="vat">*zzgl. 19 % MwSt.</div>
</section>

<section class="flyer flyer--back" aria-label="Rückseite Rundum-Sorglos-Wäscherei">
  <div class="band" style="left:0;top:79px;width:720px;height:61px"></div>
  <div class="band" style="left:0;top:147px;width:700px;height:65px"></div>

  <svg class="shape" viewBox="0 0 1145 540" aria-hidden="true">
    <path d="M1145 0 V540 H720 C640 380 620 150 735 0Z" fill="var(--magenta)"/>
    <path d="M1145 70 V540 H745 C610 440 610 200 730 70Z" fill="var(--graphite)"/>
  </svg>
  <svg class="shape" viewBox="0 0 1145 540" role="img" aria-label="Foto: Sakkos und Anzüge auf Kleiderbügeln an einer Stange">
    <defs>
      <linearGradient id="suitsPhoto" x1="0" y1="0" x2="1" y2="1">
        <stop offset="0" stop-color="#6a6b6f"/>
        <stop offset=".35" stop-color="#2f3a55"/>
        <stop offset=".65" stop-color="#3d4a6d"/>
        <stop offset="1" stop-color="#555557"/>
      </linearGradient>
    </defs>
    <path d="M1145 0 V540 H760 C640 420 650 170 772 0Z" fill="url(#suitsPhoto)"/>
  </svg>

  <h2 class="headline" style="left:30px;top:82px"><span class="lead" style="font-size:40px">IHRE</span><span class="big" style="font-size:56px">RUNDUM-SORGLOS</span></h2>
  <div class="headline" style="left:132px;top:154px"><span class="big" style="font-size:56px">WÄSCHEREI</span></div>

  <ul class="services services--left">
    <li><svg width="16" height="16" viewBox="0 0 16 16" aria-hidden="true"><path d="M1 9 L6 14 L15 1" fill="none" stroke="var(--magenta)" stroke-width="2.4"/></svg>Hotel- und Gastronomiewäsche</li>
    <li><svg width="16" height="16" viewBox="0 0 16 16" aria-hidden="true"><path d="M1 9 L6 14 L15 1" fill="none" stroke="var(--magenta)" stroke-width="2.4"/></svg>Schmutzmatten</li>
    <li><svg width="16" height="16" viewBox="0 0 16 16" aria-hidden="true"><path d="M1 9 L6 14 L15 1" fill="none" stroke="var(--magenta)" stroke-width="2.4"/></svg>Gardinenservice</li>
  </ul>
  <ul class="services services--right">
    <li><svg width="16" height="16" viewBox="0 0 16 16" aria-hidden="true"><path d="M1 9 L6 14 L15 1" fill="none" stroke="var(--magenta)" stroke-width="2.4"/></svg>Berufskleidung</li>
    <li><svg width="16" height="16" viewBox="0 0 16 16" aria-hidden="true"><path d="M1 9 L6 14 L15 1" fill="none" stroke="var(--magenta)" stroke-width="2.4"/></svg>Private Wäsche</li>
    <li><svg width="16" height="16" viewBox="0 0 16 16" aria-hidden="true"><path d="M1 9 L6 14 L15 1" fill="none" stroke="var(--magenta)" stroke-width="2.4"/></svg>Verkauf von Hotel- und<br>Gastronomietextilien</li>
  </ul>

  <div class="brand" style="left:24px;top:456px;font-size:32px">Wäscherei Talbrunn</div>
  <div class="contact" style="left:427px;top:448px;font-size:14px;line-height:20.5px">
    Lindenweg 12 – 70999 Talbrunn<br>
    Tel. +49 (0) 7100 / 23 56 80<br>
    E-Mail. info@waescherei-talbrunn.de
  </div>
</section>

</body>
</html>
```